Simple landing page for Brindleys cookbook

I need a one page landingpage where customers can order the cookbook.
This is a cookbook of a collection of recipes from our deli that we used to run.
I need a landing page where customers can come and order the book. I also need it coded. I already have the domain through hostmoxa.
I can send the file of the book through wetransfer. It's too big to upload here. Just so you get the feel that I am looking for.
I attached a simple text as an introduction to the page. But I am open to any suggestions. I want it all to be about the experience that we are sharing the recipes with everybody and that it's for sale. The book is $29.99, shipping included.
Customers have to be able to click and buy the book from it.

Coding

Coded - Design and coding required

Number of Pages Required

1 page

Font styles to use
Sans Serif

Requirements
Must have
• Same colors as the cookbook

```html
<!DOCTYPE html>
<html lang="en">
<head>
<meta charset="utf-8">
<title>Brindleys Cookbook</title>
<link rel="stylesheet" href="https://fonts.googleapis.com/css2?family=Oswald:wght@600;700&family=Quicksand:wght@500;600;700&display=swap">
<style>
:root{
  --brown:#4a2a12;
  --crimson:#c41e56;
  --crimson-dark:#a8143f;
  --lime-soft:#e4edc0;
  --lime-pale:#f3f7e6;
  --olive:#9aae3a;
  --olive-dark:#6c860f;
  --text:#4b4440;
  --white:#ffffff;
  --wood:#6b3d1c;
}
*{margin:0;padding:0;box-sizing:border-box}
html,body{width:1200px;height:2525px;overflow:hidden}
body{position:relative;background:var(--white);font-family:"Quicksand",sans-serif;color:var(--text)}
.abs{position:absolute}
.bg-curves{left:0;top:0;width:1200px;height:2525px}
.brand{display:flex;align-items:center;gap:10px;font-family:"Quicksand",sans-serif;font-weight:700;color:var(--brown)}
.brand-dot{border-radius:50%;background:var(--olive);flex:none}
.hero-logo{left:145px;top:44px;font-size:36px}
.hero-logo .brand-dot{width:22px;height:22px}
.hero-title{left:145px;top:238px;width:540px;white-space:nowrap;font-family:"Oswald",sans-serif;font-weight:700;font-size:41px;line-height:61px;letter-spacing:1.5px;color:var(--brown);text-transform:uppercase}
.btn{display:inline-flex;align-items:center;justify-content:center;height:58px;padding:0 20px;border-radius:29px;background:var(--crimson);color:var(--white);font-family:"Oswald",sans-serif;font-weight:600;font-size:16px;letter-spacing:1.5px;white-space:nowrap;text-decoration:none;text-transform:uppercase}
.hero-btn{left:145px;top:453px;width:263px}
.book-cover{left:698px;top:72px;width:370px;height:522px;border-radius:4px;background:linear-gradient(160deg,#eef1f4 0%,#d9dde0 40%,#c8a47a 62%,#a9b9a0 85%,#e7e9eb 100%);box-shadow:0 40px 40px -20px rgba(0,0,0,.18)}
.price-badge{display:flex;flex-direction:column;align-items:center;justify-content:center;border-radius:50%;background:radial-gradient(circle,var(--crimson) 60%,var(--crimson-dark) 100%);color:var(--white);box-shadow:0 0 40px rgba(196,30,86,.35)}
.price{font-family:"Oswald",sans-serif;font-weight:600;line-height:1}
.price small{font-size:.55em;vertical-align:top}
.ship{font-size:9px;font-weight:600;line-height:1.1;display:flex;align-items:center;gap:4px;margin-top:4px}
.hero-badge{left:656px;top:157px;width:122px;height:122px}
.hero-badge .price{font-size:32px}
.story{left:145px;top:692px;width:911px;height:500px;border-radius:14px;overflow:hidden;display:flex;box-shadow:0 20px 40px rgba(0,0,0,.12)}
.story-photo{width:458px;height:100%;background:linear-gradient(135deg,#1f4640 0%,#35605a 40%,#7a7a70 70%,#c9cfca 100%)}
.story-panel{position:relative;flex:1;background:linear-gradient(160deg,var(--olive) 0%,var(--olive-dark) 100%)}
.story-text{position:absolute;left:75px;top:128px;width:290px;font-size:15px;font-weight:500;line-height:26.6px;letter-spacing:.5px;color:var(--white)}
.story-text strong{font-family:"Oswald",sans-serif;font-size:21px;color:var(--brown);letter-spacing:1px;margin-right:6px}
.story-btn{position:absolute;left:67px;top:323px;width:263px}
.pickle-art{left:916px;top:1088px;width:208px;height:180px;background:linear-gradient(150deg,#b4d43a,#5f8a12);border-radius:50% 20% 50% 20%;transform:rotate(-35deg)}
.recipes-title{left:0;top:1332px;width:1200px;text-align:center;font-family:"Oswald",sans-serif;font-weight:700;font-size:48px;line-height:51px;letter-spacing:4px;color:var(--brown);text-transform:uppercase}
.recipes-sub{left:370px;top:1442px;width:460px;text-align:center;font-size:13.5px;font-weight:600;line-height:19px;letter-spacing:1px;color:#222}
.recipes-card{left:145px;top:1560px;width:520px;height:260px;background:var(--white);border-radius:12px;box-shadow:0 10px 30px rgba(0,0,0,.06)}
.recipes-text{left:191px;top:1576px;width:345px;font-size:15px;font-weight:500;line-height:26.6px;letter-spacing:.5px}
.recipes-btn{left:191px;top:1792px;width:263px}
.open-book{left:560px;top:1560px;width:640px;height:360px;border-radius:10px;transform:skewY(-14deg);background:linear-gradient(120deg,#cfd8df 0%,#e7e4df 30%,#f3efe9 60%,#dcd2c5 100%);box-shadow:0 30px 40px -20px rgba(0,0,0,.2)}
.recipes-badge{left:548px;top:1502px;width:106px;height:106px}
.recipes-badge .price{font-size:28px}
.sandwich-photo{left:0;top:1950px;width:640px;height:518px;background:radial-gradient(ellipse at 40% 55%,#e8e1cc 0%,#cfc7a8 35%,#a7a488 60%,rgba(255,255,255,0) 85%)}
.closing-logo{left:600px;top:2030px;width:265px;justify-content:center;font-size:46px}
.closing-logo .brand-dot{width:28px;height:28px}
.quote-box{left:605px;top:2180px;width:450px;height:238px;border:4px solid var(--brown);border-right:none;border-radius:12px 0 0 12px;background:var(--white)}
.quote-text{left:647px;top:2228px;width:410px;font-size:15px;font-weight:500;line-height:26.6px;letter-spacing:.5px}
.quote-mark{left:615px;top:2150px;width:62px;height:62px;border-radius:50%;background:var(--crimson);display:flex;align-items:center;justify-content:center}
.footer{left:0;top:2468px;width:1200px;height:57px;background:linear-gradient(180deg,#7a4721,var(--wood));color:#f1e6d8;font-size:14px;font-weight:600;display:flex;align-items:center;justify-content:center;letter-spacing:.3px}
</style>
</head>
<body>
<svg class="abs bg-curves" viewBox="0 0 1200 2525" aria-hidden="true">
  <defs>
    <linearGradient id="heroFade" x1="0" y1="0" x2="0" y2="1">
      <stop offset="0" stop-color="#f3f7e6"/><stop offset="1" stop-color="#ffffff"/>
    </linearGradient>
  </defs>
  <rect x="0" y="0" width="1200" height="620" fill="url(#heroFade)"/>
  <path d="M0 395 C120 250 260 140 380 130 C560 115 720 210 900 260 C1030 295 1130 290 1200 270 L1200 320 C1080 340 960 330 820 300 C640 260 500 230 380 250 C240 280 100 360 0 430 Z" fill="#e4edc0"/>
  <path d="M75 225 C140 170 220 140 300 132 C220 150 150 190 75 225 Z" fill="#ffffff"/>
  <path d="M0 1440 C200 1540 420 1560 640 1520 C860 1480 1060 1380 1200 1295 L1200 1790 C1060 1760 900 1710 760 1680 L0 1680 Z" fill="#e4edc0"/>
  <path d="M40 1560 C110 1620 170 1650 230 1660 C170 1640 110 1610 40 1560 Z" fill="#ffffff"/>
</svg>

<div class="abs brand hero-logo"><span class="brand-dot"></span>Brindleys</div>
<h1 class="abs hero-title">Your favourite Brindleys<br>recipes, now available<br>in a cook book!</h1>
<a class="abs btn hero-btn" href="#order">Order your copy here</a>
<div class="abs book-cover" role="img" aria-label="Cookbook cover showing a deli sandwich on a bun"></div>
<div class="abs price-badge hero-badge">
  <div class="price"><small>$</small>29.99</div>
  <div class="ship"><svg width="16" height="11" viewBox="0 0 16 11" fill="none" stroke="#fff" stroke-width="1.2"><rect x="1" y="1" width="9" height="6"/><path d="M10 3h3l2 2v2h-5"/><circle cx="4" cy="9" r="1.3"/><circle cx="12" cy="9" r="1.3"/></svg><span>Free<br>Shipping</span></div>
</div>

<section class="abs story">
  <div class="story-photo" role="img" aria-label="Deli storefront with green door and window signs"></div>
  <div class="story-panel">
    <p class="story-text"><strong>BRINDLEYS</strong>was a small Deli in Thornfield, NB. After it opened its doors in 2010, it quickly turned into an iconic place, where people from all over came to enjoy one of the European inspired sandwiches.</p>
    <a class="btn story-btn" href="#order">Order your copy here</a>
  </div>
</section>
<div class="abs pickle-art" role="img" aria-label="Illustrated green pickle"></div>

<h2 class="abs recipes-title">Favorite recipes<br>in one book</h2>
<p class="abs recipes-sub">We Truly Hope You Will Enjoy Making These Sandwiches Just As Much As We Did.</p>
<div class="abs recipes-card"></div>
<p class="abs recipes-text">Now the recipes are available for everybody to use in this compilation of the most favourite menu items. Simple to follow instructions – it's no rocket science! With common ingredients you will be able to whip those up in no time and enjoy for yourself or with friends.</p>
<a class="abs btn recipes-btn" href="#order" id="order">Order your copy here</a>
<div class="abs open-book" role="img" aria-label="Open cookbook showing sandwich recipe pages beside the closed cover"></div>
<div class="abs price-badge recipes-badge">
  <div class="price"><small>$</small>29.99</div>
  <div class="ship"><svg width="16" height="11" viewBox="0 0 16 11" fill="none" stroke="#fff" stroke-width="1.2"><rect x="1" y="1" width="9" height="6"/><path d="M10 3h3l2 2v2h-5"/><circle cx="4" cy="9" r="1.3"/><circle cx="12" cy="9" r="1.3"/></svg><span>Free<br>Shipping</span></div>
</div>

<div class="abs sandwich-photo" role="img" aria-label="Close-up of a focaccia sandwich with cheese and tomato"></div>
<div class="abs brand closing-logo"><span class="brand-dot"></span>Brindleys</div>
<div class="abs quote-box"></div>
<div class="abs quote-mark"><svg width="30" height="22" viewBox="0 0 30 22" fill="none" stroke="#fff" stroke-width="3" stroke-linecap="round"><circle cx="7" cy="7" r="5"/><path d="M12 7c0 7-4 11-8 13"/><circle cx="21" cy="7" r="5"/><path d="M26 7c0 7-4 11-8 13"/></svg></div>
<p class="abs quote-text">If you had the opportunity to visit Brindleys in its days and enjoy one of the sandwiches firsthand, now you can relive the glory days and make them at home! If you never had the chance to have a Brindleys sandwich, you can still get a taste of what the hype was all about.</p>

<footer class="abs footer">Copyright 2022. Marta Ellison | All Rights Reserved</footer>
</body>
</html>
```